Photographer Card

I'm currently doing freelance photography and i need a creative design name card especially when i attend events.
I require a design that makes a STATEMENT.
Simple, elegant and nothing like the usual name cards ive seen around (Example: with a camera/tripod etc in the design).

Photographer: Dorian VP
Mobile: +65 84126957
E-mail: Dorian.VP.Photography@mailvista.net
Facebook: www.friendlane.net/dorian.vp.photography

Thanks for your time and hope it will turn out well! :)
Updates

Thanks for all your inputs!

Im liking the cursive feel.

Id prefer not to include the title "freelance"  :)

Also, im looking for a logo to establish myself

http://www.artmosaic.net/art/Cotton-Business-Card-583021746

Hi all! Thanks for the designs

"Capturing magical moments"
"Capturing magical moments that are gone forever"

Back design can be in big font "look HERE"

Maybe with focusing box 

Names can be played with horizontal and vertical.

Industry/Entity Type

Camera

Font styles to use
Script

```html
<!DOCTYPE html>
<html lang="en">
<head>
<meta charset="utf-8">
<title>Dorian VP Photography — Business Card</title>
<link rel="stylesheet" href="https://fonts.googleapis.com/css2?family=Great+Vibes&family=Cormorant+Garamond:wght@500&family=Questrial&family=Roboto:wght@400&display=swap">
<style>
  :root {
    --backdrop: #e4e2de;
    --card-dark: #1a1b1d;
    --card-mid: #303134;
    --silver-light: #f4f4f4;
    --silver-mid: #b9bbbe;
    --silver-dark: #6f7276;
    --text-white: #f4f4f4;
  }
  * { margin: 0; padding: 0; box-sizing: border-box; }
  html, body {
    width: 1200px;
    height: 784px;
    overflow: hidden;
    background: var(--backdrop);
  }
  .canvas {
    position: relative;
    width: 1200px;
    height: 784px;
  }
  .card {
    position: absolute;
    top: 72px;
    width: 380px;
    height: 640px;
    border-radius: 4px;
    overflow: hidden;
    box-shadow: 0 10px 28px rgba(0,0,0,0.25);
  }
  .card--back { left: 170px; }
  .card--front { left: 650px; }
  .card__texture {
    position: absolute;
    inset: 0;
    background:
      linear-gradient(135deg, rgba(255,255,255,0.04) 0%, rgba(0,0,0,0.2) 100%),
      radial-gradient(ellipse at 50% 40%, var(--card-mid) 0%, var(--card-dark) 78%);
  }
  .card__frame {
    position: absolute;
    inset: 22px;
    border: 3px solid var(--silver-mid);
    box-shadow: inset 0 0 0 1px rgba(0,0,0,0.5), 0 0 0 1px rgba(255,255,255,0.15);
  }
  .card--front .card__frame {
    inset: 26px;
    border-width: 4px;
    border-color: var(--silver-light);
    box-shadow: 0 0 0 3px rgba(0,0,0,0.6), 0 0 0 5px var(--silver-dark);
  }

  /* Rotated content area: landscape layout turned 90° clockwise */
  .turned {
    position: absolute;
    left: 50%;
    top: 50%;
    width: 640px;
    height: 380px;
    transform: translate(-50%, -50%) rotate(90deg);
  }

  .statement {
    position: absolute;
    left: 80px;
    top: 44px;
    font-family: "Questrial", sans-serif;
    font-weight: 400;
    line-height: 0.92;
  }
  .statement__word {
    display: block;
    background: linear-gradient(180deg, var(--silver-light) 0%, var(--silver-mid) 55%, var(--silver-dark) 100%);
    -webkit-background-clip: text;
    background-clip: text;
    color: transparent;
  }
  .statement__word--big { font-size: 108px; letter-spacing: 3px; }
  .statement__word--small { font-size: 80px; margin-left: 128px; line-height: 0.85; }

  .identity {
    position: absolute;
    left: 120px;
    top: 36px;
    color: var(--text-white);
  }
  .identity__name {
    font-family: "Great Vibes", cursive;
    font-size: 80px;
    line-height: 0.95;
    font-weight: 400;
    white-space: nowrap;
  }
  .identity__title {
    font-family: "Cormorant Garamond", serif;
    font-size: 28px;
    font-weight: 500;
    letter-spacing: 1px;
    margin-left: -14px;
    margin-top: -4px;
  }
  .contact {
    position: absolute;
    left: 56px;
    top: 196px;
    list-style: none;
    font-family: "Roboto", sans-serif;
    color: var(--text-white);
    white-space: nowrap;
  }
  .contact__phone { font-size: 24px; letter-spacing: 1px; margin-bottom: 12px; margin-left: 50px; }
  .contact__email { font-size: 17px; margin-bottom: 6px; margin-left: 6px; }
  .contact__web { font-size: 14px; }
</style>
</head>
<body>
<main class="canvas">
  <section class="card card--back" aria-label="Card back">
    <div class="card__texture" role="img" aria-label="Dark carbon-fibre diagonal weave texture"></div>
    <div class="card__frame"></div>
    <div class="turned">
      <h2 class="statement">
        <span class="statement__word statement__word--big">LOOK</span>
        <span class="statement__word statement__word--small">at</span>
        <span class="statement__word statement__word--big">HERE</span>
      </h2>
    </div>
  </section>

  <section class="card card--front" aria-label="Card front">
    <div class="card__texture" role="img" aria-label="Dark background with a grid of small focusing squares"></div>
    <div class="card__frame"></div>
    <div class="turned">
      <header class="identity">
        <h1 class="identity__name">Dorian VP</h1>
        <p class="identity__title">Photography</p>
      </header>
      <ul class="contact">
        <li class="contact__phone">+65 84126957</li>
        <li class="contact__email">Dorian.VP.Photography@mailvista.net</li>
        <li class="contact__web">www.friendlane.net/dorian.vp.photography</li>
      </ul>
    </div>
  </section>
</main>
</body>
</html>
```